Informative 1-Pager website that informs users about the threat of ransomware

See current page: https://www.quellbrook-shield.com/

Coded - Design and coding required

```html
<!DOCTYPE html>
<html lang="en">
<head>
<meta charset="utf-8">
<title>Quellbrook – Learn how to protect yourself from ransomware</title>
<link href="https://fonts.googleapis.com/css2?family=Audiowide&family=Oswald:wght@500;600&family=Open+Sans:wght@400;600&family=Poppins:wght@500;600;700&display=swap" rel="stylesheet">
<style>
:root{
  --yellow:#f9c935;
  --navy:#0b1a3d;
  --navy-deep:#06112b;
  --ink:#111111;
  --text:#3a3a3a;
  --muted:#5e5e5e;
  --grey-band:#f1f1f1;
  --card:#f3f3f3;
  --footer:#0e0e0e;
  --white:#ffffff;
}
*{margin:0;padding:0;box-sizing:border-box}
html,body{width:1200px;height:3875px;overflow:hidden}
body{position:relative;background:var(--white);font-family:"Open Sans",sans-serif;color:var(--text)}
.abs{position:absolute}
.bar{position:absolute;width:57px;height:8px;background:var(--yellow)}
.h-section{font-family:"Oswald",sans-serif;font-weight:600;color:var(--ink);font-size:33px;line-height:1.3}
.btn{position:absolute;display:flex;align-items:center;justify-content:center;border-radius:32px;font-family:"Poppins",sans-serif;font-weight:600;font-size:20px;color:var(--ink);text-decoration:none;box-shadow:0 6px 14px rgba(0,0,0,.12)}
.btn-yellow{background:var(--yellow)}
.btn-white{background:var(--white)}

/* hero */
.hero{position:absolute;left:0;top:0;width:1200px;height:690px;background:linear-gradient(120deg,var(--navy-deep) 0%,#0d2a5e 45%,#0a4f8a 75%,#0a6fa6 100%);overflow:hidden}
.hero-art{position:absolute;left:640px;top:60px;width:560px;height:560px;background:radial-gradient(circle at 45% 50%,rgba(50,200,255,.75) 0%,rgba(20,120,200,.45) 30%,rgba(10,60,130,0) 65%)}
.brand{position:absolute;left:111px;top:48px;font-family:"Poppins",sans-serif;font-weight:600;font-size:24px;color:var(--white)}
.topbar{position:absolute;top:24px;left:555px;display:flex;align-items:center;gap:22px;font-family:"Audiowide",sans-serif;font-size:14px;color:var(--white)}
.topbar .sep{width:1px;height:24px;background:rgba(255,255,255,.7)}
.topbar .ic{display:inline-flex;align-items:center;gap:6px}
.socials-top{display:flex;gap:9px}
.socials-top span{width:10px;height:10px;border-radius:50%;background:var(--white)}
.topline{position:absolute;top:56px;left:510px;width:690px;height:1px;background:rgba(255,255,255,.5)}
.nav{position:absolute;top:68px;left:472px;font-family:"Audiowide",sans-serif;font-size:16px;color:var(--white)}
.nav a{color:var(--white);text-decoration:none;position:absolute;white-space:nowrap}
.nav a.active{color:var(--yellow);text-decoration:underline}
.hero-title{position:absolute;left:111px;top:205px;font-family:"Audiowide",sans-serif;font-weight:400;font-size:58px;line-height:66px;color:var(--white)}
.hero-sub{position:absolute;left:111px;top:346px;font-family:"Poppins",sans-serif;font-size:16px;color:var(--white)}
.hero-wave{position:absolute;left:0;top:540px}

/* types */
.types-sub{position:absolute;left:0;width:1200px;top:800px;text-align:center;font-size:16px;color:var(--ink)}
.card{position:absolute;top:850px;width:220px;height:287px;background:var(--card);border-radius:10px;text-align:center;padding:22px 10px 0}
.card.is-active{background:var(--yellow);box-shadow:0 8px 18px rgba(0,0,0,.15)}
.card .icon{width:72px;height:72px;border-radius:50%;background:var(--yellow);margin:0 auto 14px;display:flex;align-items:center;justify-content:center}
.card.is-active .icon{background:var(--white)}
.card h3{font-family:"Oswald",sans-serif;font-weight:500;font-size:17px;line-height:26px;color:var(--ink);margin:0 auto 8px;width:170px}
.card p{font-size:11.5px;line-height:21px;color:var(--muted)}
.card.is-active p{color:#3b3116}
.card a{display:block;margin-top:6px;font-family:"Poppins",sans-serif;font-weight:600;font-size:15px;color:var(--ink);text-decoration:underline}

/* about */
.about-band{position:absolute;left:0;top:1217px;width:1200px;height:588px;background:var(--grey-band)}
.about-frame{position:absolute;left:90px;top:1320px;width:392px;height:410px;background:var(--yellow);clip-path:polygon(0 0,100% 0,100% 95%,92% 100%,0 100%)}
.about-photo{position:absolute;left:111px;top:1298px;width:407px;height:408px;background:linear-gradient(135deg,#0e2148 0%,#1e4a8a 45%,#3fa2e0 60%,#132a55 100%)}
.p-body{font-size:16px;line-height:31px;color:var(--text)}

/* nutshell */
.video-frame{position:absolute;left:111px;top:1980px;width:976px;height:418px;background:var(--yellow);box-shadow:0 10px 20px rgba(0,0,0,.1)}
.video-still{position:absolute;left:122px;top:1992px;width:954px;height:396px;background:linear-gradient(100deg,#0f2b78 0%,#1d3fa0 30%,#c8562a 45%,#1b6e8a 62%,#1fb2b0 75%,#0e2a68 100%)}
.play{position:absolute;left:570px;top:2160px;width:56px;height:56px;border-radius:50%;background:var(--white);display:flex;align-items:center;justify-content:center}
.dots{position:absolute;left:1004px;top:2320px;width:120px;height:116px;background:rgba(0,0,0,.06)}

/* avoid */
.avoid-band{position:absolute;left:0;top:2472px;width:711px;height:612px;background:var(--yellow)}
.avoid-photo{position:absolute;left:600px;top:2556px;width:488px;height:438px;border:4px solid var(--white);background:linear-gradient(140deg,#d9e6f2 0%,#5f86a8 35%,#1b2c45 70%,#0e1826 100%)}

/* newsletter */
.news-form{position:absolute;left:218px;top:3248px;width:764px;height:68px;border-radius:34px;background:var(--white);box-shadow:0 6px 18px rgba(0,0,0,.1);overflow:hidden}
.news-form .field{position:absolute;left:36px;top:0;line-height:68px;font-size:15px;color:#555}
.news-form .submit{position:absolute;right:0;top:0;width:218px;height:68px;border-radius:34px;background:var(--yellow);font-family:"Poppins",sans-serif;font-weight:600;font-size:26px;color:var(--ink);display:flex;align-items:center;justify-content:center}

/* footer */
.footer{position:absolute;left:0;top:3404px;width:1200px;height:471px;background:var(--footer);color:var(--white)}
.f-col{position:absolute;top:88px}
.f-col h4{font-family:"Oswald",sans-serif;font-weight:500;font-size:21px;color:var(--white)}
.f-col .rule{width:26px;height:2px;background:var(--white);margin:14px 0 18px}
.f-col ul{list-style:none}
.f-col li{font-size:16px;line-height:34.5px;display:flex;align-items:center;gap:10px}
.f-contact li{align-items:flex-start;line-height:24px;margin-bottom:12px}
.f-contact .c-ic{width:26px;height:26px;border-radius:50%;border:2px solid var(--white);display:flex;align-items:center;justify-content:center;flex:none}
.f-about p{font-size:14px;line-height:26px;width:236px;text-align:justify}
.f-social{display:flex;gap:14px;margin-top:18px}
.f-social span{width:32px;height:32px;border-radius:50%;border:2px solid var(--white)}
.f-divider{position:absolute;left:119px;top:366px;width:980px;height:1px;background:rgba(255,255,255,.45)}
.copy{position:absolute;left:0;width:1200px;top:400px;text-align:center;font-size:15px}
</style>
</head>
<body>

<header class="hero">
  <div class="hero-art" role="img" aria-label="Glowing digital padlock over streams of binary code"></div>
  <div class="brand">Quellbrook</div>
  <div class="topbar">
    <span class="ic"><svg width="12" height="12" viewBox="0 0 24 24"><path fill="#fff" d="M6.6 10.8a15 15 0 0 0 6.6 6.6l2.2-2.2c.3-.3.7-.4 1-.2 1.1.4 2.3.6 3.6.6.6 0 1 .4 1 1V20c0 .6-.4 1-1 1A17 17 0 0 1 3 4c0-.6.4-1 1-1h3.5c.6 0 1 .4 1 1 0 1.3.2 2.5.6 3.6.1.3 0 .7-.2 1z"/></svg>+1 555 014 2290</span>
    <span class="sep"></span>
    <span class="ic"><svg width="13" height="11" viewBox="0 0 24 18"><path fill="#fff" d="M0 0h24v18H0zM2 2l10 7 10-7z"/></svg>info@quellbrook-shield.com</span>
    <span class="sep"></span>
    <span class="socials-top"><span></span><span></span><span></span><span></span></span>
  </div>
  <div class="topline"></div>
  <nav class="nav">
    <a class="active" style="left:0">Home</a>
    <a style="left:99px">About</a>
    <a style="left:196px">Types</a>
    <a style="left:294px">Avoid a Ransomware</a>
    <a style="left:523px">Contact Us</a>
  </nav>
  <h1 class="hero-title">Welcome To<br>Ransomware</h1>
  <p class="hero-sub">Learn how to protect yourself from ransomware</p>
  <a class="btn btn-yellow" style="left:111px;top:392px;width:168px;height:60px;font-size:20px">Get Started</a>
  <svg class="hero-wave" width="1200" height="150" viewBox="0 0 1200 150">
    <path d="M0 70 C70 30 150 30 200 60 C260 100 290 150 380 140 C470 130 520 60 620 75 C720 90 760 150 880 140 C990 130 1060 80 1120 60 C1160 45 1185 30 1200 20 L1200 150 L0 150 Z" fill="#fff"/>
    <path d="M0 70 C70 30 150 30 200 60 C260 100 290 150 380 140 C470 130 520 60 620 75 C720 90 760 150 880 140 C990 130 1060 80 1120 60 C1160 45 1185 30 1200 20" fill="none" stroke="#f9c935" stroke-width="7"/>
  </svg>
</header>

<section aria-label="Ransomware types">
  <div class="bar" style="left:571px;top:728px"></div>
  <h2 class="h-section abs" style="left:0;width:1200px;top:740px;text-align:center">What are Common Ransomware Types?</h2>
  <p class="types-sub">There are many different types of ransomware. Here are four typical categories:</p>

  <article class="card" style="left:111px">
    <div class="icon"><svg width="36" height="34" viewBox="0 0 36 34" fill="none" stroke="#222" stroke-width="2"><rect x="3" y="3" width="30" height="20" rx="2"/><path d="M13 30h10M18 23v7"/></svg></div>
    <h3>Ransomware that fakes something</h3>
    <p>Scareware fakes a problem on the computer. For example, it could be a warning that a virus or malware has been found on the PC.</p>
    <a>Read More</a>
  </article>
  <article class="card" style="left:363px">
    <div class="icon"><svg width="36" height="34" viewBox="0 0 36 34" fill="none" stroke="#222" stroke-width="2"><rect x="4" y="8" width="28" height="20" rx="2"/><circle cx="18" cy="18" r="5"/></svg></div>
    <h3>Ransomware that encrypts something</h3>
    <p>Encryptors are the most common type of ransomware that encrypts all data and requires a key to unlock it, which.</p>
    <a>Read More</a>
  </article>
  <article class="card is-active" style="left:615px">
    <div class="icon"><svg width="36" height="36" viewBox="0 0 36 36" fill="none" stroke="#222" stroke-width="2"><rect x="6" y="16" width="16" height="14" rx="2"/><path d="M9 16v-4a5 5 0 0 1 10 0v4"/><path d="M26 6h4v4h-4zM24 14h3M30 14h2"/></svg></div>
    <h3 style="width:130px">Ransomware that leaks data</h3>
    <p>This type of ransomware is called Doxware. Doxware often tries to force the user or the company to pay by threatening.</p>
    <a>Read More</a>
  </article>
  <article class="card" style="left:867px">
    <div class="icon"><svg width="36" height="30" viewBox="0 0 36 30" fill="none" stroke="#222" stroke-width="2"><rect x="3" y="3" width="30" height="24" rx="2"/><path d="M3 5l15 11L33 5"/></svg></div>
    <h3 style="width:140px">Ransomware that locks something</h3>
    <p>Instead of preventing access to files or applications, this ransomware type prevent the end user's device from being used.</p>
    <a>Read More</a>
  </article>
</section>

<section aria-label="About ransomware">
  <div class="about-band"></div>
  <div class="about-frame"></div>
  <div class="about-photo" role="img" aria-label="Hand holding a glowing shield with a padlock among network lines"></div>
  <div class="bar" style="left:581px;top:1307px"></div>
  <h2 class="h-section abs" style="left:581px;top:1328px">About Ransomware</h2>
  <div class="abs p-body" style="left:581px;top:1387px;width:510px">
    <p>Veltrane (company registration number CHE-418.207.561) was started in 2018 as a public limited company in Zug, Switzerland. Our analysts have long-standing relationships with various players on the Darknet.</p>
    <p style="margin-top:31px">These personal relationships make it possible for Veltrane to repeatedly obtain the latest data leaks. Those unique data leaks are published by the press around the world.</p>
  </div>
  <a class="btn btn-yellow" style="left:580px;top:1661px;width:167px;height:62px">Read More</a>
</section>

<section aria-label="Ransomware in a nutshell">
  <div class="bar" style="left:111px;top:1885px"></div>
  <h2 class="h-section abs" style="left:111px;top:1903px">Ransomware in a Nutshell</h2>
  <p class="abs" style="left:517px;top:1866px;width:570px;font-size:15.5px;line-height:29px;color:var(--text)">Ransomware is a very dangerous cyber threat to all organisations and individuals. Ransomware is a type of malicious software that may block access to files or devices until the victim pays a ransom.</p>
  <div class="dots" role="img" aria-label="Dotted decoration"></div>
  <div class="video-frame"></div>
  <div class="video-still" role="img" aria-label="Video still: a cyber shield with keyhole over lines of source code"></div>
  <div class="play"><svg width="22" height="24" viewBox="0 0 22 24"><path d="M3 1l18 11L3 23z" fill="#111"/></svg></div>
</section>

<section aria-label="How to avoid a ransomware attack">
  <div class="avoid-band"></div>
  <div class="abs" style="left:111px;top:2549px;width:65px;height:8px;background:var(--ink)"></div>
  <h2 class="h-section abs" style="left:111px;top:2566px;line-height:51px;width:460px">How can you avoid a Ransomware Attack?</h2>
  <div class="abs p-body" style="left:111px;top:2669px;width:462px;color:var(--ink);font-size:15.5px">
    <p>The best defense is the right behavior. Be suspicious of all downloads, attachments, etc. and only run software if you trust the creator.</p>
    <p style="margin-top:31px">This includes macros in office applications. Also, keep your operating system and all applications patched and up to date to ensure that you have fewer vulnerabilities that a hacker can exploit.</p>
  </div>
  <a class="btn btn-white" style="left:111px;top:2927px;width:168px;height:62px">Read More</a>
  <div class="avoid-photo" role="img" aria-label="Businessman touching a network of glowing padlock shields"></div>
</section>

<section aria-label="Newsletter">
  <div class="bar" style="left:571px;top:3164px"></div>
  <h2 class="h-section abs" style="left:0;width:1200px;top:3180px;text-align:center">Join our Newsletter</h2>
  <div class="news-form">
    <span class="field">Enter The Email</span>
    <span class="submit">Subscribe</span>
  </div>
</section>

<footer class="footer">
  <div class="f-col" style="left:119px">
    <h4>Quick Links</h4><div class="rule"></div>
    <ul><li>→ Home</li><li>→ About</li><li>→ Services</li><li>→ Our Clients</li><li>→ Contact Us</li></ul>
  </div>
  <div class="f-col" style="left:333px">
    <h4>Help Links</h4><div class="rule"></div>
    <ul><li>→ FAQ</li><li>→ Terms</li><li>→ Privacy Policy</li><li>→ Support Links</li><li>→ Conditions</li></ul>
  </div>
  <div class="f-col f-contact" style="left:572px">
    <h4>Contact Us</h4><div class="rule"></div>
    <ul>
      <li><span class="c-ic"><svg width="10" height="13" viewBox="0 0 10 13"><path d="M5 0a5 5 0 0 0-5 5c0 3.5 5 8 5 8s5-4.5 5-8a5 5 0 0 0-5-5zm0 7a2 2 0 1 1 0-4 2 2 0 0 1 0 4z" fill="#fff"/></svg></span><span>2471 Harlow Lane<br>United States</span></li>
      <li><span class="c-ic"><svg width="12" height="9" viewBox="0 0 24 18"><path fill="#fff" d="M0 0h24v18H0zM2 2l10 7 10-7z"/></svg></span><span>info@quellbrook-shield.com</span></li>
      <li><span class="c-ic"><svg width="11" height="11" viewBox="0 0 24 24"><path fill="#fff" d="M6.6 10.8a15 15 0 0 0 6.6 6.6l2.2-2.2c.3-.3.7-.4 1-.2 1.1.4 2.3.6 3.6.6.6 0 1 .4 1 1V20c0 .6-.4 1-1 1A17 17 0 0 1 3 4c0-.6.4-1 1-1h3.5c.6 0 1 .4 1 1 0 1.3.2 2.5.6 3.6.1.3 0 .7-.2 1z"/></svg></span><span>+1 555 014 2290</span></li>
    </ul>
  </div>
  <div class="f-col f-about" style="left:853px">
    <h4>About Ransomware</h4><div class="rule"></div>
    <p>Veltrane (company registration number CHE-418.207.561) was started in 2018 as a public limited company in Zug, Switzerland.</p>
    <div class="f-social"><span></span><span></span><span></span><span></span></div>
  </div>
  <div class="f-divider"></div>
  <p class="copy">Copyrights@2022.Quellbrook.All Rights Reserved</p>
</footer>

</body>
</html>
```